New business card for civil engineering company - "Keystone Audit"

We need a business card designed for our new structural engineering company.

The company name is "Keystone Audit" logo files attached.

We would like the following:
* Two-sided card
* Simple design

Information to be placed on the card:
Name - Marcus Dellow
Job Title - Director / Structural Engineer
Credentials - BEng(Hons), CPEng, CMengNZ, IntPE(NZ)
Email - marcus.dellow@keystoneaudit.co.nz
mobile - 0219364058
website - www.keystoneaudit.co.nz

```html
<!DOCTYPE html>
<html lang="en">
<head>
<meta charset="utf-8">
<title>Keystone Audit – Business Card</title>
<link rel="stylesheet" href="https://fonts.googleapis.com/css2?family=Jost:wght@300;400;500&display=swap">
<style>
  :root {
    --backdrop: #2a2a2d;
    --card: #f5f5f5;
    --brand-blue: #3f7fd6;
    --text-grey: #555659;
    --tab-grey: #dedfe3;
    --mark-blue: #4a88dc;
  }
  * { margin: 0; padding: 0; box-sizing: border-box; }
  html, body {
    width: 1200px; height: 900px; overflow: hidden;
    background: var(--backdrop);
    font-family: "Jost", sans-serif;
  }
  .card {
    position: absolute; left: 250px;
    width: 700px; height: 400px;
    background: var(--card);
    box-shadow: 0 6px 18px rgba(0,0,0,.35);
  }
  .card--front { top: 30px; }
  .card--back { top: 470px; }

  .person { position: absolute; left: 92px; top: 150px; }
  .person__name {
    font-weight: 300; font-size: 36px; letter-spacing: 1px;
    color: var(--brand-blue); text-transform: uppercase; line-height: 1;
  }
  .person__role, .person__credentials {
    font-weight: 400; font-size: 15px; color: var(--text-grey); line-height: 1.35;
  }
  .person__role { margin-top: 16px; }

  .contacts { position: absolute; left: 0; top: 268px; list-style: none; }
  .contacts__item { display: flex; align-items: center; height: 30px; margin-bottom: 6px; }
  .contacts__tab {
    width: 92px; height: 26px; background: var(--tab-grey);
    display: flex; justify-content: flex-end; align-items: center; padding-right: 10px;
  }
  .contacts__tab svg { width: 14px; height: 14px; fill: var(--brand-blue); }
  .contacts__text { margin-left: 16px; font-size: 15px; color: var(--text-grey); letter-spacing: .3px; }

  .brand { display: flex; align-items: center; gap: 10px; }
  .brand__square { width: 18px; height: 18px; background: var(--mark-blue); }
  .brand__name {
    font-weight: 500; font-size: 20px; letter-spacing: 2px;
    color: var(--text-grey); text-transform: uppercase;
  }
  .card--front .brand { position: absolute; right: 40px; top: 78px; }
  .card--back .brand {
    position: absolute; left: 50%; top: 50%; transform: translate(-50%, -50%);
  }
  .card--back .brand__square { width: 26px; height: 26px; }
  .card--back .brand__name { font-size: 30px; letter-spacing: 3px; }
</style>
</head>
<body>
  <section class="card card--front">
    <div class="brand">
      <span class="brand__square"></span>
      <span class="brand__name">Keystone Audit</span>
    </div>
    <div class="person">
      <h1 class="person__name">Marcus Dellow</h1>
      <p class="person__role">Director / Structural Engineer</p>
      <p class="person__credentials">BEng(Hons), CPEng, CMengNZ, IntPE(NZ)</p>
    </div>
    <ul class="contacts">
      <li class="contacts__item">
        <span class="contacts__tab"><svg viewBox="0 0 24 24"><path d="M6.6 10.8a15 15 0 0 0 6.6 6.6l2.2-2.2a1 1 0 0 1 1-.25 11.4 11.4 0 0 0 3.6.57 1 1 0 0 1 1 1V20a1 1 0 0 1-1 1A17 17 0 0 1 3 4a1 1 0 0 1 1-1h3.5a1 1 0 0 1 1 1c0 1.25.2 2.45.57 3.6a1 1 0 0 1-.25 1z"/></svg></span>
        <span class="contacts__text">021 9364 058</span>
      </li>
      <li class="contacts__item">
        <span class="contacts__tab"><svg viewBox="0 0 24 24"><path d="M2 5h20v14H2z M4 7v.4l8 5.2 8-5.2V7z" fill-rule="evenodd"/></svg></span>
        <span class="contacts__text">marcus.dellow@keystoneaudit.co.nz</span>
      </li>
      <li class="contacts__item">
        <span class="contacts__tab"><svg viewBox="0 0 24 24"><path d="M12 2a10 10 0 1 0 0 20 10 10 0 0 0 0-20zm-1 17.9A8 8 0 0 1 4.1 13H7c.1 2.5.8 4.9 2 6.9zM7 11H4.1A8 8 0 0 1 9 4.1 14 14 0 0 0 7 11zm6 8.9V13h4a14 14 0 0 1-4 6.9zM13 11V4.1A14 14 0 0 1 17 11zm2 8A14 14 0 0 0 19 13h.9A8 8 0 0 1 15 19zm4-8a14 14 0 0 0-4-6.9A8 8 0 0 1 19.9 11zM11 4.1V11H9a14 14 0 0 1 2-6.9zM11 13v6.9A14 14 0 0 1 9 13z"/></svg></span>
        <span class="contacts__text">www.keystoneaudit.co.nz</span>
      </li>
    </ul>
  </section>

  <section class="card card--back">
    <div class="brand">
      <span class="brand__square"></span>
      <span class="brand__name">Keystone Audit</span>
    </div>
  </section>
</body>
</html>
```